Electrical contractor in San Diego county since 1988

Provide a company name/ logo for business cards and forms. Newer and more modern old card is attached. Color preference is black and orange. Simple and streamlined nothing too busy. I have also attached a card that represents the simplicity of what we are looking for.

Contractor

```html
<!DOCTYPE html>
<html lang="en">
<head>
<meta charset="utf-8">
<title>K.M. Electric Inc. – Business Card</title>
<link rel="stylesheet" href="https://fonts.googleapis.com/css2?family=Baloo+2:wght@500;700&family=Barlow+Semi+Condensed:wght@400;500&family=Marcellus&family=PT+Serif:wght@700&display=swap">
<style>
  :root {
    --ink: #000000;
    --signal-orange: #F7941D;
    --burnt-orange: #A85A14;
    --muted-orange: #B9752E;
  }
  html, body {
    margin: 0;
    padding: 0;
    overflow: hidden;
    background: var(--ink);
  }
  .card {
    position: relative;
    width: 1200px;
    height: 702px;
    background: var(--ink);
    overflow: hidden;
  }
  .header-band {
    position: absolute;
    left: 0;
    top: 60px;
    width: 1200px;
    height: 153px;
    background: var(--signal-orange);
  }
  .brand-mark {
    position: absolute;
    left: 82px;
    top: 84px;
    width: 96px;
    height: 96px;
    border-radius: 50%;
    background: var(--ink);
  }
  .company-name {
    position: absolute;
    left: 0;
    width: 1200px;
    top: 84px;
    margin: 0;
    text-align: center;
    font-family: "Baloo 2", sans-serif;
    font-weight: 700;
    font-size: 48px;
    line-height: 1;
    letter-spacing: 1px;
    color: var(--ink);
  }
  .company-tagline {
    position: absolute;
    left: 0;
    width: 1200px;
    top: 134px;
    margin: 0;
    text-align: center;
    font-family: "Baloo 2", sans-serif;
    font-weight: 500;
    font-size: 50px;
    line-height: 1;
    color: var(--ink);
  }
  .license {
    position: absolute;
    left: 973px;
    top: 178px;
    margin: 0;
    font-family: "PT Serif", serif;
    font-weight: 700;
    font-size: 34px;
    line-height: 1;
    letter-spacing: -0.5px;
    transform: scaleX(0.88);
    transform-origin: left center;
    color: var(--ink);
  }
  .person-name {
    position: absolute;
    left: 0;
    width: 1200px;
    top: 294px;
    margin: 0;
    text-align: center;
    font-family: "Barlow Semi Condensed", sans-serif;
    font-weight: 500;
    font-size: 66px;
    line-height: 1;
    color: var(--signal-orange);
  }
  .person-title {
    position: absolute;
    left: 0;
    width: 1200px;
    top: 362px;
    margin: 0;
    text-align: center;
    font-family: "Barlow Semi Condensed", sans-serif;
    font-weight: 400;
    font-size: 50px;
    line-height: 1;
    color: var(--muted-orange);
  }
  .contact-line {
    position: absolute;
    left: 0;
    width: 1200px;
    top: 462px;
    margin: 0;
    text-align: center;
    font-family: "Marcellus", serif;
    font-size: 44px;
    line-height: 1;
  }
  .contact-label { color: var(--muted-orange); }
  .contact-value { color: var(--signal-orange); }
  .footer-band {
    position: absolute;
    left: 0;
    top: 580px;
    width: 1200px;
    height: 67px;
    background: var(--burnt-orange);
  }
  .mailing-address {
    position: absolute;
    left: 0;
    width: 1200px;
    top: 593px;
    margin: 0;
    text-align: center;
    font-family: "Marcellus", serif;
    font-size: 39px;
    line-height: 1;
    color: var(--ink);
  }
</style>
</head>
<body>
  <div class="card">
    <div class="header-band"></div>
    <div class="brand-mark" aria-hidden="true"></div>
    <h1 class="company-name">K.M. ELECTRIC INC.</h1>
    <p class="company-tagline">Commercial - New &amp; Remodel</p>
    <p class="license">Lic. 704318</p>

    <h2 class="person-name">DANIEL MARSH</h2>
    <p class="person-title">PRESIDENT</p>

    <p class="contact-line">
      <span class="contact-label">Tel:</span>
      <span class="contact-value">(555) 014-2283</span>
      <span class="contact-label">- Fax:</span>
      <span class="contact-value">014-2290</span>
    </p>

    <div class="footer-band"></div>
    <p class="mailing-address">P.O. Box 4471, Brookdale, CA 90000-0471</p>
  </div>
</body>
</html>
```